Business Card Design Project

Lorabelle is a women fashion house focusing on youthful glamour.

We bring together unique designs, premium quality materials and top craftsmanship to deliver sophisticated yet playful glamour, fun and excitement to the confident woman.

We can sum up the brand identity in 3 words:
Glamour – Sophistication – Unique

Industry/Entity Type

Fashion

Requirements
Must have
• Nim Terassa
nim.terassa@lorabelle.example
Mobile: 090 361 8847
Instragram: lorabelle_label
Facebook: lorabelle

Creative Director
Lorabelle Co., LTD
TEL: 02 613 49 87
41 Rose Court, 2nd Floor , C Building , Thonglor , Rama Road 27.
South Bangchak , Phrao Nuan , Bangkok 10990 Thailand
www.lorabelle.example

```html
<!DOCTYPE html>
<html lang="en">
<head>
<meta charset="utf-8">
<title>Lorabelle Business Card Options</title>
<link rel="stylesheet" href="https://fonts.googleapis.com/css2?family=Prompt:wght@300;400&display=swap">
<style>
  :root {
    --sheet: #4a4a4a;
    --card: #ffffff;
    --ink: #111111;
    --muted: #606060;
    --band: #000000;
    --band-text: #ffffff;
    --rule: #9a9a9a;
  }
  * { margin: 0; padding: 0; box-sizing: border-box; }
  html, body { width: 1200px; height: 1000px; overflow: hidden; }
  body {
    position: relative;
    background: var(--sheet);
    font-family: "Prompt", "Helvetica Neue", Arial, sans-serif;
    font-weight: 300;
    color: var(--ink);
  }
  .option-number {
    position: absolute;
    font-size: 78px;
    line-height: 1;
    font-weight: 400;
    color: var(--ink);
  }
  .card {
    position: absolute;
    left: 307px;
    width: 586px;
    height: 335px;
    background: var(--card);
  }
  .card--one { top: 142px; }
  .card--two { top: 522px; }
  .brand-name {
    position: absolute;
    font-size: 50px;
    font-weight: 300;
    line-height: 1;
    letter-spacing: 0.5px;
    color: var(--ink);
  }
  .divider {
    position: absolute;
    left: 293px;
    top: 20px;
    width: 1px;
    height: 233px;
    background: linear-gradient(to bottom, transparent, var(--rule) 20%, var(--rule) 80%, transparent);
  }
  .person { position: absolute; }
  .person__name {
    font-size: 19px;
    font-weight: 300;
    line-height: 22px;
    letter-spacing: 0.2px;
    color: var(--ink);
  }
  .person__role {
    font-size: 13px;
    line-height: 17px;
    color: var(--muted);
  }
  .contacts { position: absolute; list-style: none; }
  .contacts li {
    display: flex;
    align-items: center;
    height: 21px;
    font-size: 13.5px;
    color: var(--muted);
    white-space: nowrap;
  }
  .contacts svg {
    width: 14px;
    height: 14px;
    margin-right: 13px;
    flex: none;
    fill: var(--ink);
  }
  .address-band {
    position: absolute;
    left: 0;
    bottom: 0;
    width: 100%;
    height: 62px;
    background: var(--band);
    color: var(--band-text);
    font-size: 13.5px;
    line-height: 18.5px;
    text-align: center;
    padding-top: 15px;
    white-space: nowrap;
  }
  .pin {
    position: absolute;
    left: 281px;
    top: -13px;
    width: 24px;
    height: 24px;
  }
</style>
</head>
<body>

<svg width="0" height="0" style="position:absolute" aria-hidden="true">
  <defs>
    <symbol id="icon-mail" viewBox="0 0 14 14"><path d="M0 3h14v9H0z" fill="#111"/><path d="M1 4l6 4.2L13 4" fill="none" stroke="#fff" stroke-width="1.2"/></symbol>
    <symbol id="icon-mobile" viewBox="0 0 14 14"><rect x="3.5" y="0.5" width="7" height="13" rx="1.2"/><rect x="5" y="2" width="4" height="8.5" fill="#fff"/></symbol>
    <symbol id="icon-phone" viewBox="0 0 14 14"><path d="M3 0.5l2.5 3-1.5 1.8c0.9 2 2.5 3.6 4.6 4.6l1.8-1.5 3 2.5-1.6 2.4C6.5 13 1 7.5 0.8 2.2z"/></symbol>
    <symbol id="icon-square" viewBox="0 0 14 14"><rect x="1" y="1" width="12" height="12" rx="1.5"/></symbol>
    <symbol id="icon-globe" viewBox="0 0 14 14"><g fill="none" stroke="#111" stroke-width="1.1"><circle cx="7" cy="7" r="6"/><ellipse cx="7" cy="7" rx="2.6" ry="6"/><path d="M1 7h12M2 4h10M2 10h10"/></g></symbol>
    <symbol id="icon-pin" viewBox="0 0 24 24"><circle cx="12" cy="12" r="12" fill="#000"/><path d="M12 5.5a3.8 3.8 0 0 0-3.8 3.8c0 2.8 3.8 7.2 3.8 7.2s3.8-4.4 3.8-7.2A3.8 3.8 0 0 0 12 5.5z" fill="#fff"/><circle cx="12" cy="9.3" r="1.4" fill="#000"/></symbol>
  </defs>
</svg>

<div class="option-number" style="left:171px; top:262px;">1</div>
<section class="card card--one">
  <div class="brand-name" style="left:30px; top:114px;">Lorabelle</div>
  <div class="divider"></div>
  <div class="person" style="left:348px; top:42px;">
    <p class="person__name">NIM TERASSA</p>
    <p class="person__role">Creative Director</p>
  </div>
  <ul class="contacts" style="left:349px; top:112px;">
    <li><svg><use href="#icon-mail"/></svg>nim.terassa@lorabelle.example</li>
    <li><svg><use href="#icon-mobile"/></svg>090 361 8847</li>
    <li><svg><use href="#icon-phone"/></svg>02 613 49 87</li>
    <li><svg><use href="#icon-square"/></svg>lorabelle_label</li>
    <li><svg><use href="#icon-globe"/></svg>www.lorabelle.example</li>
    <li><svg><use href="#icon-square"/></svg>lorabelle</li>
  </ul>
  <div class="address-band">
    <svg class="pin"><use href="#icon-pin"/></svg>
    Lorabelle Co., LTD - 41 Rose Court, 2nd Floor , C Building , Thonglor , Rama Road 27.<br>
    South Bangchak , Phrao Nuan , Bangkok 10990 Thailand
  </div>
</section>

<div class="option-number" style="left:171px; top:634px;">2</div>
<section class="card card--two">
  <div class="brand-name" style="left:48px; top:30px;">Lorabelle</div>
  <div class="person" style="left:63px; top:109px;">
    <p class="person__name">NIM TERASSA</p>
    <p class="person__role">Creative Director,<br>Lorabelle Co., LTD</p>
  </div>
  <ul class="contacts" style="left:336px; top:108px;">
    <li><svg><use href="#icon-mail"/></svg>nim.terassa@lorabelle.example</li>
    <li><svg><use href="#icon-mobile"/></svg>090 361 8847</li>
    <li><svg><use href="#icon-phone"/></svg>02 613 49 87</li>
    <li><svg><use href="#icon-square"/></svg>lorabelle_label</li>
    <li><svg><use href="#icon-globe"/></svg>www.lorabelle.example</li>
    <li><svg><use href="#icon-square"/></svg>lorabelle</li>
  </ul>
  <div class="address-band">
    <svg class="pin"><use href="#icon-pin"/></svg>
    41 Rose Court, 2nd Floor , C Building , Thonglor , Rama Road 27.<br>
    South Bangchak , Phrao Nuan , Bangkok 10990 Thailand
  </div>
</section>

</body>
</html>
```